Stonelynk Business Card Design

The Stonelynk Co is an aggregate (crushing) equipment dealer serving Western Canadian provinces. Stonelynk is a distributor of aggregate equipment for different manufacturers.

We are looking to change and update the existing business card which has been used since the existence of the company. A copy of existing card has been attached for reference. The Stonelynk Co logo we want to remain the same and we want the green color to remain the same.

We are wanting something new with a different look. A refreshing card to show a new modern and updated look. No longer wanting to have the manufacturers on the back of the card but something more like our logo on the back of the card with a statement like "Crushing Solutions"

ideas could be:
- card can be different colors on front and back
- front or reverse of the card could possibly be the green color with the logo in black

Target Market(s)

Owners of Aggregate/Crushing companies

Requirements
Must have
• - logo to remain same along with same font within logo
• - green color to remain same
Nice to have
• as noted above under project description
Should not have

```html
<!DOCTYPE html>
<html lang="en">
<head>
<meta charset="utf-8">
<title>Stonelynk Business Card</title>
<link href="https://fonts.googleapis.com/css2?family=Raleway:wght@500;600;700;800&family=Open+Sans:wght@400;600&display=swap" rel="stylesheet">
<style>
  :root {
    --backdrop: #d4d4d2;
    --brand-green: #8f8c34;
    --ink: #231f20;
    --paper: #ffffff;
    --text-dark: #1e1e1e;
  }
  * { box-sizing: border-box; margin: 0; padding: 0; }
  html, body { width: 1200px; height: 1000px; overflow: hidden; }
  body {
    position: relative;
    background: var(--backdrop);
    font-family: "Raleway", sans-serif;
  }
  .card {
    position: absolute;
    width: 630px;
    height: 362px;
    border-radius: 36px;
    overflow: hidden;
    background: var(--paper);
  }
  .card-front { left: 149px; top: 101px; }
  .card-back { left: 373px; top: 548px; }

  .front-band {
    position: absolute; left: 0; top: 0; width: 100%; height: 294px;
    background: var(--brand-green);
  }
  .front-name {
    position: absolute; left: 0; top: 206px; width: 100%;
    display: flex; justify-content: center; align-items: center; gap: 14px;
    font-weight: 800; font-size: 31px; letter-spacing: 0.5px; color: var(--ink);
  }
  .front-name .mark-dot {
    width: 22px; height: 22px; border-radius: 50%; background: var(--ink);
  }
  .product-line {
    position: absolute; left: 0; top: 314px; width: 100%;
    display: flex; justify-content: center; align-items: center;
    font-weight: 500; font-size: 20px; letter-spacing: 0.6px; color: var(--text-dark);
  }
  .product-line span + span { border-left: 2px solid var(--text-dark); margin-left: 12px; padding-left: 12px; line-height: 26px; }

  .back-band {
    position: absolute; left: 0; top: 0; width: 100%; height: 180px;
    background: var(--brand-green);
  }
  .holder-name {
    position: absolute; left: 27px; top: 112px;
    font-weight: 500; font-size: 28px; letter-spacing: 0.5px; color: var(--paper);
  }
  .back-name {
    position: absolute; left: 368px; top: 120px;
    font-weight: 800; font-size: 16px; letter-spacing: 0.3px; color: var(--paper);
  }
  .address-tab {
    position: absolute; left: 97px; top: 180px; width: 436px; height: 32px;
    background: var(--ink); border-radius: 0 0 30px 30px;
    display: flex; justify-content: center; align-items: center;
    font-family: "Open Sans", sans-serif; font-size: 14.5px; letter-spacing: 0.4px; color: var(--paper);
  }
  .contact-list { position: absolute; list-style: none; }
  .contact-phones { left: 26px; top: 236px; }
  .contact-web { left: 313px; top: 236px; }
  .contact-list li {
    display: flex; align-items: center; height: 34.5px;
    font-family: "Open Sans", sans-serif; font-size: 23px; color: var(--text-dark);
  }
  .contact-list svg { width: 19px; height: 19px; margin-right: 19px; fill: var(--text-dark); flex: none; }
  .contact-web svg { margin-right: 14px; }
</style>
</head>
<body>

<section class="card card-front" aria-label="Card front">
  <div class="front-band">
    <div class="front-name"><span class="mark-dot"></span>THE STONELYNK CO.</div>
  </div>
  <div class="product-line"><span>SCREENERS</span><span>CRUSHERS</span><span>STACKERS</span></div>
</section>

<section class="card card-back" aria-label="Card back">
  <div class="back-band">
    <div class="holder-name">DALE MORROW</div>
    <div class="back-name">THE STONELYNK CO.</div>
  </div>
  <div class="address-tab">2290-48B STREET, NISKU, ALBERTA T9E 2K1</div>

  <ul class="contact-list contact-phones">
    <li>
      <svg viewBox="0 0 20 20" aria-hidden="true"><path d="M2 7c0-2 3-3.5 8-3.5S18 5 18 7v1.5h-4V7H6v1.5H2z"/><path d="M4 10h12l1 7H3z"/><circle cx="10" cy="13.5" r="2" fill="#fff"/></svg>
      780 . 555 . 0142
    </li>
    <li>
      <svg viewBox="0 0 20 20" aria-hidden="true"><path d="M5 2l3 4-2 2c1 2.5 3.5 5 6 6l2-2 4 3-2 3C9 18 2 11 2 4z"/></svg>
      780 . 555 . 0187
    </li>
    <li>
      <svg viewBox="0 0 20 20" aria-hidden="true"><path d="M5 2h10v5H5z"/><path d="M2 8h16v7h-3v-3H5v3H2z"/><path d="M6 13h8v5H6z"/></svg>
      780 . 555 . 0163
    </li>
  </ul>

  <ul class="contact-list contact-web">
    <li>
      <svg viewBox="0 0 20 20" aria-hidden="true"><path d="M2 5h16v10H2z"/><path d="M2 5l8 6 8-6" fill="none" stroke="#fff" stroke-width="1.5"/></svg>
      dale@stonel.com
    </li>
    <li>
      <svg viewBox="0 0 20 20" aria-hidden="true"><circle cx="10" cy="10" r="8" fill="none" stroke="#1e1e1e" stroke-width="1.8"/><ellipse cx="10" cy="10" rx="3.5" ry="8" fill="none" stroke="#1e1e1e" stroke-width="1.5"/><path d="M2 10h16M3.5 6h13M3.5 14h13" stroke="#1e1e1e" stroke-width="1.4"/></svg>
      www.stonelynk.ca
    </li>
  </ul>
</section>

</body>
</html>
```